Company Banner

I would like our 5 corporate Core Values placed on a single banner that has a theme related to our engineering industry.

Core Values: Productive & Hard Working, Professional, Humble, Personable, Adaptable

Target Market(s)

Construction, Engineering

Requirements
Must have
• All words randomly positioned on the banner with color and industry background images.

Please add company logo to upper left corner as well (attached logo design file)

```html
<!DOCTYPE html>
<html lang="en">
<head>
<meta charset="UTF-8">
<title>Core Values Banner</title>
<link href="https://fonts.googleapis.com/css2?family=Bebas+Neue&family=Oswald:wght@500;600&display=swap" rel="stylesheet">
<style>
  :root {
    --navy: #0b1350;
    --navy-deep: #070d3c;
    --white: #f7f7f7;
    --title-shadow: #8c8f9c;
    --orange: #e56424;
    --blue: #0a74e0;
    --yellow: #dfba22;
    --red: #e33447;
    --green: #a3b945;
  }
  html, body {
    margin: 0;
    padding: 0;
    width: 944px;
    height: 1200px;
    overflow: hidden;
    background: var(--navy);
  }
  .banner {
    position: relative;
    width: 944px;
    height: 1200px;
    background: radial-gradient(ellipse at 50% 40%, #0f1a5c 0%, var(--navy) 55%, var(--navy-deep) 100%);
    overflow: hidden;
  }
  .banner__title {
    position: absolute;
    top: 108px;
    left: 0;
    width: 100%;
    margin: 0;
    text-align: center;
    font-family: "Bebas Neue", sans-serif;
    font-weight: 400;
    font-size: 150px;
    line-height: 1;
    letter-spacing: 1px;
    color: var(--white);
    text-shadow: 4px 5px 0 var(--title-shadow);
  }
  .values-wheel {
    position: absolute;
    top: 0;
    left: 0;
  }
  .value-label {
    font-family: "Oswald", sans-serif;
    font-weight: 600;
    font-size: 30px;
    fill: var(--white);
    letter-spacing: 0.5px;
  }
  .value-label--long { font-size: 27px; }
  .hub__number {
    font-family: "Bebas Neue", sans-serif;
    font-size: 120px;
    fill: var(--white);
  }
  .hub__words {
    font-family: "Bebas Neue", sans-serif;
    font-size: 50px;
    fill: var(--white);
  }
</style>
</head>
<body>
<div class="banner">
  <h1 class="banner__title">Core Values</h1>

  <svg class="values-wheel" width="944" height="1200" viewBox="0 0 944 1200" xmlns="http://www.w3.org/2000/svg">
    <defs>
      <linearGradient id="tone-welding" x1="0" y1="0" x2="1" y2="1">
        <stop offset="0" stop-color="#8a8479"/>
        <stop offset="0.55" stop-color="#4d6a78"/>
        <stop offset="1" stop-color="#b08a55"/>
      </linearGradient>
      <linearGradient id="tone-lab" x1="0" y1="0" x2="1" y2="1">
        <stop offset="0" stop-color="#6f7f86"/>
        <stop offset="0.5" stop-color="#3c4a52"/>
        <stop offset="1" stop-color="#7f8b6e"/>
      </linearGradient>
      <linearGradient id="tone-team" x1="0" y1="0" x2="1" y2="1">
        <stop offset="0" stop-color="#c9d1da"/>
        <stop offset="1" stop-color="#4a5866"/>
      </linearGradient>
      <linearGradient id="tone-portrait" x1="0" y1="0" x2="1" y2="1">
        <stop offset="0" stop-color="#e4e4e4"/>
        <stop offset="1" stop-color="#b9b3b0"/>
      </linearGradient>
      <linearGradient id="tone-site" x1="0" y1="0" x2="1" y2="1">
        <stop offset="0" stop-color="#8d9296"/>
        <stop offset="0.5" stop-color="#c5c8ca"/>
        <stop offset="1" stop-color="#4d5155"/>
      </linearGradient>

      <path id="arc-top" d="M291,410.8 A308,308 0 0 1 653,410.8"/>
      <path id="arc-right" d="M653,410.8 A308,308 0 0 1 764.9,755.2"/>
      <path id="arc-left" d="M179.1,755.2 A308,308 0 0 1 291,410.8"/>
      <path id="arc-bottom-right" d="M472,992 A332,332 0 0 0 787.8,762.6"/>
      <path id="arc-bottom-left" d="M156.2,762.6 A332,332 0 0 0 472,992"/>
    </defs>

    <!-- outer coloured bands -->
    <g class="value-bands">
      <path d="M472,660 L266.3,376.8 A350,350 0 0 1 677.7,376.8 Z" fill="var(--orange)"/>
      <path d="M472,660 L677.7,376.8 A350,350 0 0 1 804.9,768.2 Z" fill="var(--blue)"/>
      <path d="M472,660 L804.9,768.2 A350,350 0 0 1 472,1010 Z" fill="var(--yellow)"/>
      <path d="M472,660 L472,1010 A350,350 0 0 1 139.1,768.2 Z" fill="var(--red)"/>
      <path d="M472,660 L139.1,768.2 A350,350 0 0 1 266.3,376.8 Z" fill="var(--green)"/>
    </g>

    <!-- image areas -->
    <g class="value-images">
      <path role="img" aria-label="Photo of a welder at work with sparks" d="M472,660 L301.5,425.4 A290,290 0 0 1 642.5,425.4 Z" fill="url(#tone-welding)"/>
      <path role="img" aria-label="Photo of an engineer inspecting lab equipment" d="M472,660 L642.5,425.4 A290,290 0 0 1 747.8,749.6 Z" fill="url(#tone-lab)"/>
      <path role="img" aria-label="Photo of an engineering team working together at a workstation" d="M472,660 L747.8,749.6 A290,290 0 0 1 472,950 Z" fill="url(#tone-team)"/>
      <path role="img" aria-label="Photo of a smiling worker in a hard hat" d="M472,660 L472,950 A290,290 0 0 1 196.2,749.6 Z" fill="url(#tone-portrait)"/>
      <path role="img" aria-label="Photo of construction workers in safety gear on site" d="M472,660 L196.2,749.6 A290,290 0 0 1 301.5,425.4 Z" fill="url(#tone-site)"/>
    </g>

    <!-- inner coloured ring -->
    <g class="value-ring">
      <path d="M472,660 L389.7,546.7 A140,140 0 0 1 554.3,546.7 Z" fill="var(--orange)"/>
      <path d="M472,660 L554.3,546.7 A140,140 0 0 1 605.2,703.3 Z" fill="var(--blue)"/>
      <path d="M472,660 L605.2,703.3 A140,140 0 0 1 472,800 Z" fill="var(--yellow)"/>
      <path d="M472,660 L472,800 A140,140 0 0 1 338.8,703.3 Z" fill="var(--red)"/>
      <path d="M472,660 L338.8,703.3 A140,140 0 0 1 389.7,546.7 Z" fill="var(--green)"/>
    </g>

    <!-- hub -->
    <circle cx="472" cy="660" r="112" fill="var(--navy)"/>

    <!-- dividers -->
    <g class="value-dividers" stroke="var(--navy)" stroke-width="10" stroke-linecap="butt">
      <line x1="472" y1="660" x2="262" y2="371"/>
      <line x1="472" y1="660" x2="682" y2="371"/>
      <line x1="472" y1="660" x2="811" y2="770"/>
      <line x1="472" y1="660" x2="472" y2="1016"/>
      <line x1="472" y1="660" x2="133" y2="770"/>
    </g>
    <circle cx="472" cy="660" r="112" fill="var(--navy)"/>

    <!-- labels -->
    <text class="value-label value-label--long"><textPath href="#arc-top" startOffset="50%" text-anchor="middle">PRODUCTIVE &amp; HARD WORKING</textPath></text>
    <text class="value-label"><textPath href="#arc-right" startOffset="50%" text-anchor="middle">PROFESSIONAL</textPath></text>
    <text class="value-label"><textPath href="#arc-bottom-right" startOffset="50%" text-anchor="middle">HUMBLE</textPath></text>
    <text class="value-label"><textPath href="#arc-bottom-left" startOffset="50%" text-anchor="middle">PERSONABLE</textPath></text>
    <text class="value-label"><textPath href="#arc-left" startOffset="50%" text-anchor="middle">ADAPTABLE</textPath></text>

    <!-- hub text -->
    <text class="hub__number" x="404" y="702">5</text>
    <text class="hub__words" x="452" y="655">CORE</text>
    <text class="hub__words" x="452" y="703">VALUES</text>
  </svg>
</div>
</body>
</html>
```